Web Design for a Biotech Consulting Firm

We need a web site design for a new business based in Philadelphia called VorentaMx. This is a consulting firm that will serve medical diagnostics industry, which is part of the life science/healthcare industry focusing on developing and marketing products that help in early detection, monitoring or management of diseases. Our consulting firm will help medical diagnostic companies to overcome key challenges in designing, evaluating and marketing new products.Our company name is VorentaMx. Vorenta is Latin word for "something" Dx represents diagnostics. The idea behind the name is that we help companies to transform the original, early product ideas ("nothing") into "something"; which is a product with full clinical utility that will help to improve health and well-being.The web site should use the visual feel of the logo (attached), be modern, simple and clean looking and represent creativity, innovation, scientific thinking and progress.
Updates

Wix Design is acceptable

Industry/Entity Type

Biotechnology

Coding

Coded - Design and coding required

Number of Pages Required

1 page

Font styles to use
Sans Serif

Requirements
Must have
• simple, clean look couple of pages
Should not have
• a lot of pages

```html
<!DOCTYPE html>
<html lang="en">
<head>
<meta charset="utf-8">
<title>VorentaMx – Biotech Consulting</title>
<link href="https://fonts.googleapis.com/css2?family=Montserrat:wght@400;600;700&family=Open+Sans:wght@400;600&display=swap" rel="stylesheet">
<style>
:root{
  --blue:#1f80dc;
  --blue-dark:#1669b8;
  --ink:#2b2b2b;
  --text:#555;
  --muted:#8a8a8a;
  --grey-bg:#f1f2f4;
  --white:#fff;
  --line:#dcdcdc;
}
*{box-sizing:border-box;margin:0;padding:0}
html,body{width:1200px;height:2996px;overflow:hidden}
body{font-family:"Open Sans",sans-serif;color:var(--text);background:var(--white);position:relative}
h1,h2,h3,h4,.nav,.btn{font-family:"Montserrat",sans-serif}

/* header */
.site-header{position:absolute;top:0;left:0;width:1200px;height:108px;background:var(--white)}
.brand{position:absolute;left:112px;top:22px;height:64px;padding:0 18px;border:2px solid var(--ink);display:flex;align-items:center;gap:10px;font-family:"Montserrat",sans-serif;font-weight:600;font-size:24px;color:var(--ink)}
.brand .dot{width:12px;height:12px;background:var(--blue)}
.nav{position:absolute;left:420px;top:30px;display:flex;gap:14px;font-size:15px}
.nav a{padding:12px 20px;color:var(--ink);text-decoration:none}
.nav a.active{border:1px solid var(--line);color:var(--blue)}
.call{position:absolute;right:110px;top:26px;font-family:"Montserrat",sans-serif}
.call small{display:block;font-size:17px;color:var(--ink);letter-spacing:1px}
.call strong{display:block;font-size:24px;color:var(--blue);border-top:2px solid var(--blue);margin-top:4px;padding-top:2px}

/* hero */
.hero{position:absolute;top:108px;left:0;width:1200px;height:652px;background:linear-gradient(100deg,#2f3b4c 0%,#6d8aa8 35%,#a9c3dc 60%,#d8e2ea 100%)}
.hero-copy{position:absolute;left:112px;top:226px;width:440px;color:var(--white)}
.hero-copy h1{font-size:29px;line-height:1.35;font-weight:700}
.hero-copy .btn{display:inline-block;margin-top:24px;font-size:15px;font-weight:600;color:var(--white);padding-bottom:4px;border-bottom:2px solid var(--white)}

/* section titles */
.section-title{position:absolute;left:0;width:1200px;text-align:center;font-weight:400;font-size:36px;color:var(--ink)}
.section-title .accent{color:var(--blue)}
.rule{position:absolute;left:570px;width:60px;height:3px;background:var(--blue)}

/* welcome */
.lead{position:absolute;left:0;width:1200px;text-align:center;color:var(--blue);font-size:15px;line-height:1.6}
.intro{position:absolute;left:160px;width:880px;text-align:center;font-size:13px;line-height:1.6}
.pillar{position:absolute;top:984px;display:flex;gap:18px;width:380px}
.pillar .icon{width:60px;height:60px;border:2px solid var(--ink);display:flex;align-items:center;justify-content:center;flex:none}
.pillar h4{font-size:16px;color:var(--ink);margin-bottom:6px}
.pillar p{font-size:12px;line-height:1.6}

/* services */
.services{position:absolute;top:1132px;left:0;width:1200px;height:488px;background:var(--grey-bg)}
.service{position:absolute;top:224px;width:300px;text-align:center}
.service .icon{width:80px;height:80px;margin:0 auto 14px;display:flex;align-items:center;justify-content:center}
.service .icon.boxed{background:#dcebf9;border:2px solid var(--blue)}
.service h3{font-size:19px;color:var(--ink);margin-bottom:10px;white-space:nowrap}
.service p{font-size:13px;line-height:1.6}
.read-more{display:inline-block;margin-top:16px;padding:8px 16px;border:1px solid #bbb;font-size:13px;color:var(--ink);font-family:"Montserrat",sans-serif}

/* news */
.news-card{position:absolute;top:1748px;width:300px}
.news-card .date{display:inline-block;background:var(--blue);color:var(--white);font-size:13px;padding:6px 14px;font-family:"Montserrat",sans-serif}
.news-card h4{font-size:14px;color:var(--ink);margin:18px 0 10px;white-space:nowrap}
.news-card p{font-size:12.5px;line-height:1.6}
.news-card .more{display:inline-block;margin-top:12px;font-size:12px;color:var(--ink);border-bottom:1px solid var(--ink)}
.arrow{position:absolute;width:24px;height:40px}

/* cta */
.cta{position:absolute;top:2092px;left:0;width:1200px;height:236px;background:linear-gradient(90deg,#17181b 0%,#2a2c31 60%,#3c3f45 100%)}
.cta h2{position:absolute;left:112px;top:72px;color:var(--white);font-size:34px;font-weight:600}
.cta p{position:absolute;left:112px;top:124px;width:520px;color:#bbb;font-size:13px;line-height:1.6}
.cta .btn{position:absolute;left:880px;top:96px;color:var(--white);font-size:18px;font-weight:600;letter-spacing:1px;padding:10px 40px 10px 8px;border-bottom:2px solid var(--white)}

/* partners */
.partner{position:absolute;top:2512px;width:140px;height:64px;border:1px solid var(--line);display:flex;align-items:center;justify-content:center;font-family:"Montserrat",sans-serif;font-weight:600;font-size:17px;color:#666;background:var(--white)}
.partner.selected{border-color:var(--blue)}

/* footer */
.site-footer{position:absolute;top:2640px;left:0;width:1200px;height:320px;background:var(--blue);color:var(--white)}
.col{position:absolute;top:36px}
.col h4{font-size:16px;font-weight:600;padding-bottom:10px;margin-bottom:18px;border-bottom:1px solid rgba(255,255,255,.4)}
.col ul{list-style:none;font-size:13px;line-height:2.3}
.col ul li::before{content:"› ";}
.contact-row{display:flex;gap:12px;font-size:13px;line-height:1.5;margin-bottom:14px}
.field{width:200px;height:28px;background:var(--white);margin-bottom:10px;color:#999;font-size:12px;padding:5px 10px}
.submit{display:inline-block;background:var(--ink);padding:7px 22px;font-size:12px;font-weight:600;font-family:"Montserrat",sans-serif}
.social{display:flex;align-items:center;gap:12px;font-size:12px;margin-bottom:14px;letter-spacing:1px}
.social .circle{width:26px;height:26px;border-radius:50%;border:1px solid var(--white)}
.copyright{position:absolute;top:2960px;left:0;width:1200px;height:36px;background:var(--blue-dark);color:var(--white);text-align:center;font-size:12px;line-height:36px}
</style>
</head>
<body>

<header class="site-header">
  <div class="brand"><span>VorentaMx</span><span class="dot"></span></div>
  <nav class="nav">
    <a class="active">Home</a><a>About Us</a><a>Services</a><a>Contact Us</a>
  </nav>
  <div class="call"><small>Call Us Today</small><strong>123-555-0190</strong></div>
</header>

<section class="hero" role="img" aria-label="Photo of business people shaking hands in front of a glass office tower">
  <div class="hero-copy">
    <h1>We Are A Biotech Consulting Firm Serving The Medical Diagnostics Industry</h1>
    <span class="btn">Learn More</span>
  </div>
</section>

<h2 class="section-title" style="top:770px">Welcome To Vorenta Mx</h2>
<div class="rule" style="top:820px"></div>
<p class="lead" style="top:830px">Vorenta Dx This Is A Consulting Firm That Will Serve Medical Diagnostics Industry,<br>Which Is Part Of The Life Science/healthcare Industry</p>
<p class="intro" style="top:884px">Lorem ipsum dolor sit amet, consectetuer adipiscing elit, sed diam nonummy nibh euismod tincidunt ut laoreet dolore magna aliquam erat volutpat. Ut wisi enim ad minim veniam, quis nostrud exerci tation ullamcorper suscipit lobortis nisl ut aliquip ex ea commodo consequat. Duis autem vel eum iriure dolor in hendrerit in vulputate velit esse molestie consequat, vel illum dolore eu feugiat nulla facilisis at vero eros et accumsan.</p>

<div class="pillar" style="left:180px">
  <div class="icon"><svg width="34" height="34" viewBox="0 0 34 34" fill="none" stroke="#2b2b2b" stroke-width="2"><path d="M4 30 L17 6 L30 30 Z"/><path d="M17 6 V2 H24 V6 H17"/></svg></div>
  <div><h4>MISSION</h4><p>Lorem ipsum dolor sit amet, consectetuer adipiscing elit, sed diam nonummy nibh euismod tincidunt ut.</p></div>
</div>
<div class="pillar" style="left:640px">
  <div class="icon"><svg width="36" height="24" viewBox="0 0 36 24" fill="none" stroke="#2b2b2b" stroke-width="2"><path d="M2 12 Q18 -4 34 12 Q18 28 2 12 Z"/><circle cx="18" cy="12" r="5"/></svg></div>
  <div><h4>VISON</h4><p>Lorem ipsum dolor sit amet, consectetuer adipiscing elit, sed diam nonummy nibh euismod tincidunt ut.</p></div>
</div>

<section class="services" role="img" aria-label="Faint background photo of a researcher's hands with documents">
  <h2 class="section-title" style="top:94px">Our Services</h2>
  <div class="rule" style="top:144px"></div>
  <p class="lead" style="top:162px;color:var(--ink)">Our Consulting Firm Will Help Medical Diagnostic Companies To Overcome Key Challenges In</p>
  <div class="service" style="left:150px">
    <div class="icon"><svg width="56" height="50" viewBox="0 0 56 50" fill="none" stroke="#2b2b2b" stroke-width="2.5"><path d="M28 10 C20 4 8 4 4 8 V44 C8 40 20 40 28 46 C36 40 48 40 52 44 V8 C48 4 36 4 28 10 Z"/><path d="M28 10 V46"/></svg></div>
    <h3>Designing</h3><p>Lorem ipsum dolor sit amet, consectetuer<br>adipiscing elit , sed diam nonummy</p><span class="read-more">READ MORE ›</span>
  </div>
  <div class="service" style="left:450px">
    <div class="icon boxed"><svg width="44" height="48" viewBox="0 0 44 48" fill="none" stroke="#1f80dc" stroke-width="2.5"><rect x="6" y="6" width="32" height="38"/><rect x="15" y="2" width="14" height="8"/><path d="M13 22 l4 4 l8 -8"/><path d="M13 34 H31"/></svg></div>
    <h3 style="color:var(--blue)">Evaluating</h3><p>Lorem ipsum dolor sit amet, consectetuer<br>adipiscing elit , sed diam nonummy</p><span class="read-more" style="border-color:var(--blue);color:var(--blue)">READ MORE ›</span>
  </div>
  <div class="service" style="left:750px">
    <div class="icon"><svg width="60" height="50" viewBox="0 0 60 50" fill="none" stroke="#2b2b2b" stroke-width="2.5"><rect x="4" y="4" width="52" height="34"/><path d="M22 46 H38 M30 38 V46"/><path d="M12 30 V22 M22 30 V14 M32 30 V18 M42 30 V10"/></svg></div>
    <h3>Marketing New Products</h3><p>Lorem ipsum dolor sit amet, consectetuer<br>adipiscing elit , sed diam nonummy</p><span class="read-more">READ MORE ›</span>
  </div>
</section>

<h2 class="section-title" style="top:1646px">Latest <span class="accent">News</span></h2>
<div class="rule" style="top:1696px"></div>
<svg class="arrow" style="left:52px;top:1812px" viewBox="0 0 24 40"><path d="M18 6 L6 20 L18 34" fill="none" stroke="#999" stroke-width="3"/></svg>
<svg class="arrow" style="left:1124px;top:1812px" viewBox="0 0 24 40"><path d="M6 6 L18 20 L6 34" fill="none" stroke="#999" stroke-width="3"/></svg>
<article class="news-card" style="left:112px"><span class="date">JUNE 16, 2018</span><h4>LOREM IPSUM DOLOR SIT AMET NEE</h4><p>Quis nostrud exerci tation ullamcorper suscipit lobortis nisl ut aliquip ex ea commodo consequat. Duis autem vel eum iriure</p><span class="more">READ MORE</span></article>
<article class="news-card" style="left:450px"><span class="date">JUNE 16, 2018</span><h4>SED DIAM NONUMMY NIBH EUISMOD</h4><p>Quis nostrud exerci tation ullamcorper suscipit lobortis nisl ut aliquip ex ea commodo consequat. Duis autem vel eum iriure</p><span class="more">READ MORE</span></article>
<article class="news-card" style="left:790px"><span class="date">JUNE 16, 2018</span><h4>LOREM IPSUM DOLOR SIT AMET NEE</h4><p>Quis nostrud exerci tation ullamcorper suscipit lobortis nisl ut aliquip ex ea commodo consequat. Duis autem vel eum iriure</p><span class="more">READ MORE</span></article>

<section class="cta" role="img" aria-label="Dark photo of a hand drawing on a glass board">
  <h2>Not Sure of Your Next Step?</h2>
  <p>Lorem ipsum dolor sit amet, consectetuer adipiscing elit, sed nonummy nibh euismod tincidunt ut laoreet dolore.</p>
  <span class="btn">GET STARTED ›</span>
</section>

<h2 class="section-title" style="top:2424px">Our <span class="accent">Partners</span></h2>
<div class="rule" style="top:2474px"></div>
<svg class="arrow" style="left:40px;top:2524px" viewBox="0 0 24 40"><path d="M18 6 L6 20 L18 34" fill="none" stroke="#999" stroke-width="3"/></svg>
<svg class="arrow" style="left:1136px;top:2524px" viewBox="0 0 24 40"><path d="M6 6 L18 20 L6 34" fill="none" stroke="#999" stroke-width="3"/></svg>
<div class="partner selected" style="left:112px">Kestrelab</div>
<div class="partner" style="left:276px">Pendrift</div>
<div class="partner" style="left:440px">Corvane</div>
<div class="partner" style="left:604px">Lumetra</div>
<div class="partner" style="left:768px">Tovari</div>
<div class="partner" style="left:932px">Brisken</div>

<footer class="site-footer">
  <div class="col" style="left:112px;width:180px"><h4>Quick Links</h4>
    <ul><li>Home</li><li>About Us</li><li>Services</li><li>Contact Us</li></ul></div>
  <div class="col" style="left:324px;width:240px"><h4>Contact Details</h4>
    <div class="contact-row"><svg width="14" height="18" viewBox="0 0 14 18"><path d="M7 1 C3 1 1 4 1 7 C1 11 7 17 7 17 C7 17 13 11 13 7 C13 4 11 1 7 1 Z" fill="#fff"/><circle cx="7" cy="7" r="2.3" fill="#1f80dc"/></svg><span>48 Harlow Lane, Suite 210<br>Philadelphia, PA 19103</span></div>
    <div class="contact-row"><svg width="16" height="16" viewBox="0 0 16 16"><path d="M3 1 L6 1 L7 5 L5 6.5 C6 9 7 10 9.5 11 L11 9 L15 10 L15 13 C15 14 14 15 13 15 C6 15 1 10 1 3 C1 2 2 1 3 1 Z" fill="#fff"/></svg><span>123-555-0190</span></div>
    <div class="contact-row"><svg width="16" height="12" viewBox="0 0 16 12"><rect x="0.5" y="0.5" width="15" height="11" fill="none" stroke="#fff"/><path d="M1 1 L8 7 L15 1" fill="none" stroke="#fff"/></svg><span>hello@vorentamx.example</span></div>
  </div>
  <div class="col" style="left:636px;width:220px"><h4>Quick Inquiry</h4>
    <div class="field">Name</div><div class="field">Email</div><div class="field">Message</div><span class="submit">SUBMIT</span></div>
  <div class="col" style="left:972px;width:120px"><h4>Follow Us</h4>
    <div class="social"><span class="circle"></span>PINWAVE</div>
    <div class="social"><span class="circle"></span>CHIRPNET</div>
    <div class="social"><span class="circle"></span>LINKLOOM</div></div>
</footer>
<div class="copyright">Copyright © 2018 VorentaMx. All Rights Reserved.</div>

</body>
</html>
```